Catering company looking to promote business

We need a flyer design for our company named "Berry Good Bites." We cater/deliver açaí bowls and smoothies.

The objective of this flyer is to let companies know that we are taking açaí bowls and smoothie orders and they can be delivered to them.

Some key points we would like on the flyer:
- Photo of açaí bowl and smoothie
- Menu w/ pricing
- "No hidden delivery fees"
- 5 bowl or smoothie minimum
- Online ordering through website:
https://shopkiosk.example/store/berrygoodbites
- For the month of February --> Get one free topping and drizzle!
- FRIDAY DELIVERIES ONLY
- Questions? Call (555) 417-9832
- social media chatterbook & snapgram @bgbites
- website www.berrygoodbites.example

font - hello beautiful

Target Market(s)

Juice, smoothies, açaí bowls

Industry/Entity Type

Business

Font styles to use
Other font styles liked:
• Hello Beautiful

Colors
a64599
b768aa
d3a5cc
eedced
f7f1f7
9bcb3c

Requirements
Must have
• Please match logo, fonts, color schemes, etc.

```html
<!DOCTYPE html>
<html lang="en">
<head>
<meta charset="utf-8">
<title>Berry Good Bites – Catering Flyer</title>
<link rel="stylesheet" href="https://fonts.googleapis.com/css2?family=Amatic+SC:wght@700&family=Didact+Gothic&display=swap">
<style>
  :root {
    --plum: #a64599;
    --orchid: #b768aa;
    --mauve: #d3a5cc;
    --blush: #eedced;
    --mist: #f7f1f7;
    --lime: #9bcb3c;
    --ink: #000000;
    --paper: #e9e6e2;
    --white: #ffffff;
  }
  * { box-sizing: border-box; margin: 0; padding: 0; }
  html, body { width: 1200px; height: 1200px; overflow: hidden; }
  body { background: var(--paper); font-family: "Didact Gothic", sans-serif; color: var(--white); position: relative; }

  .flyer { position: absolute; top: 220px; width: 513px; height: 726px; background: var(--ink); overflow: hidden; box-shadow: 0 4px 10px rgba(0,0,0,.25); }
  .flyer--front { left: 73px; }
  .flyer--menu { left: 614px; }
  .abs { position: absolute; }
  .heading { font-family: "Amatic SC", cursive; font-weight: 700; line-height: 1; }
  .centered { left: 0; right: 0; text-align: center; }

  /* front */
  .hero-photo { left: 0; top: 0; width: 513px; height: 420px;
    background: radial-gradient(circle at 45% 42%, #c9b7a6 0 18%, #7a3b4f 30%, transparent 48%),
                linear-gradient(180deg, #2f5a42 0%, #23402f 45%, #000 100%); }
  .logo { left: 380px; top: 48px; width: 130px; display: flex; align-items: center; gap: 6px; }
  .logo__dot { width: 16px; height: 16px; border-radius: 50%; background: var(--lime); flex: none; }
  .logo__name { font-family: "Amatic SC", cursive; font-weight: 700; font-size: 22px; color: var(--orchid); line-height: .95; }
  .tagline { top: 408px; font-size: 40px; color: var(--orchid); }
  .subline { top: 452px; font-size: 17px; letter-spacing: .5px; }
  .thumb { width: 125px; height: 88px; border: 2px solid var(--plum); }
  .thumb--smoothie { left: 122px; top: 484px; transform: rotate(-2deg); background: linear-gradient(135deg, #d8d4cf, #5a1e33 55%, #2a1a18); }
  .thumb--bowl { left: 263px; top: 486px; transform: rotate(2deg); background: radial-gradient(circle at 50% 40%, #d3415b 0 20%, #8a2d55 45%, #151515 80%); }
  .ribbon { left: 0; top: 576px; width: 513px; height: 26px; }
  .ribbon__text { top: 580px; font-size: 16px; color: #1a1a1a; letter-spacing: .5px; }
  .order-title { top: 620px; font-size: 24px; color: var(--lime); }
  .order-url { top: 648px; font-size: 13.5px; }
  .fine-print { font-size: 7.5px; letter-spacing: .3px; text-transform: uppercase; }
  .fine-print--front { top: 665px; color: var(--orchid); }
  .contact { font-size: 9.5px; letter-spacing: .3px; }
  .contact--front { top: 690px; }
  .footer-bars { left: 0; bottom: 0; width: 513px; height: 16px; display: flex; }
  .footer-bars__main { background: var(--plum); width: 325px; }
  .footer-bars__rest { background: var(--mauve); flex: 1; margin-left: 2px; }

  /* menu */
  .brush { left: 0; width: 513px; }
  .bowl-title { left: 36px; top: 60px; font-size: 38px; }
  .bowl-desc { left: 40px; top: 126px; width: 243px; font-size: 13px; line-height: 16.5px; text-align: justify; letter-spacing: .4px; }
  .bowl-photo { left: 317px; top: 56px; width: 166px; height: 130px; border: 2px solid var(--plum); transform: rotate(3deg);
    background: radial-gradient(circle at 50% 35%, #d3415b 0 18%, #7a2a4c 40%, #1a1a1a 80%); }
  .extra-title { top: 240px; font-size: 40px; }
  .menu-col { top: 318px; width: 170px; text-align: center; }
  .menu-col__title { font-size: 24px; margin-bottom: 6px; }
  .menu-col__title--lime { color: var(--lime); }
  .menu-col__title--orchid { color: var(--orchid); }
  .menu-col__item { font-size: 13.5px; line-height: 16.6px; letter-spacing: .3px; }
  .promo { left: 0; top: 494px; width: 513px; height: 164px; background: var(--lime); }
  .promo__title { top: 532px; font-size: 40px; color: var(--ink); }
  .promo__offer { top: 576px; font-size: 17px; line-height: 21px; letter-spacing: .5px; }
  .fine-print--menu { top: 640px; color: #1d2a0a; }
  .photo-strip { left: 0; top: 658px; width: 513px; height: 52px;
    background: linear-gradient(90deg, #cfc6bb, #4a4f6a 35%, #d2d2d2 55%, #c2333d 80%, #8c1e2a); opacity: .75; }
  .contact--menu { top: 690px; color: #e6e6e6; }
</style>
</head>
<body>

<section class="flyer flyer--front" aria-label="Catering flyer front">
  <div class="abs hero-photo" role="img" aria-label="Photo of an açaí bowl topped with bananas, strawberries and blueberries held over green leaves"></div>
  <div class="abs logo"><span class="logo__dot"></span><span class="logo__name">Berry Good Bites</span></div>

  <h1 class="abs centered heading tagline">WE CATER &amp; DELIVER</h1>
  <p class="abs centered subline">HEALTY FOOD DIRECTLY TO YOU</p>

  <div class="abs thumb thumb--smoothie" role="img" aria-label="Photo of a hand holding a berry smoothie cup"></div>
  <div class="abs thumb thumb--bowl" role="img" aria-label="Photo of a hand holding an açaí bowl cup"></div>

  <svg class="abs ribbon" viewBox="0 0 513 26" aria-hidden="true">
    <path d="M0 4 L40 2 L200 3 L380 1 L513 3 L513 22 L420 24 L250 23 L90 25 L0 23 Z" fill="var(--mauve)"/>
    <path d="M0 8 L513 6 L513 18 L0 19 Z" fill="var(--orchid)" opacity=".55"/>
  </svg>
  <p class="abs centered ribbon__text">•&nbsp; SMOOTHIES &nbsp;•&nbsp; ACAI BOWLS &nbsp;•</p>

  <h2 class="abs centered heading order-title">ONLINE ORDER</h2>
  <p class="abs centered order-url">https://shopkiosk.example/store/berrygoodbites</p>
  <p class="abs centered fine-print fine-print--front">* No hidden delivery fees * *5 bowls or smoothies minimum*</p>
  <p class="abs centered contact contact--front">(555) 417-9832 | www.berrygoodbites.example | @bgbites</p>

  <div class="abs footer-bars"><span class="footer-bars__main"></span><span class="footer-bars__rest"></span></div>
</section>

<section class="flyer flyer--menu" aria-label="Catering flyer menu">
  <svg class="abs brush" style="top:48px;height:62px" viewBox="0 0 286 62" preserveAspectRatio="none" width="286" height="62" aria-hidden="true">
    <path d="M0 10 L120 6 L240 2 L268 8 L286 18 L270 32 L282 44 L200 52 L90 56 L0 58 Z" fill="var(--orchid)" opacity=".85"/>
    <path d="M0 22 L270 20 L270 36 L0 40 Z" fill="var(--mauve)" opacity=".4"/>
  </svg>
  <h2 class="abs heading bowl-title">ACAI BOWLS $9</h2>
  <p class="abs bowl-desc">Açaí sorbet topped with granola, bananas, strawberries, blueberries, coconut shavings and drizzled with honey</p>
  <div class="abs bowl-photo" role="img" aria-label="Photo of a hand holding an açaí bowl cup"></div>

  <svg class="abs brush" style="top:228px;height:64px" viewBox="0 0 513 64" preserveAspectRatio="none" width="513" height="64" aria-hidden="true">
    <path d="M0 8 L160 4 L330 0 L513 6 L513 56 L360 60 L180 62 L0 58 Z" fill="var(--lime)" opacity=".75"/>
    <path d="M0 18 L513 16 L513 46 L0 48 Z" fill="var(--lime)" opacity=".55"/>
  </svg>
  <h2 class="abs centered heading extra-title">ADD SOMETHING EXTRA</h2>

  <div class="abs menu-col" style="left:29px">
    <h3 class="heading menu-col__title menu-col__title--lime">FRUIT $1</h3>
    <p class="menu-col__item">Bananas</p><p class="menu-col__item">Strawberries</p><p class="menu-col__item">Blueberries</p>
  </div>
  <div class="abs menu-col" style="left:175px">
    <h3 class="heading menu-col__title menu-col__title--orchid">TOPPINGS .50 ¢</h3>
    <p class="menu-col__item">Almonds</p><p class="menu-col__item">Chia Seeds</p><p class="menu-col__item">Hemp Seeds</p><p class="menu-col__item">Cacao Nibs</p><p class="menu-col__item">Quinoa Puffs</p><p class="menu-col__item">Coconut Shavings</p><p class="menu-col__item">Granola</p>
  </div>
  <div class="abs menu-col" style="left:327px">
    <h3 class="heading menu-col__title menu-col__title--lime">DRIZZLE .50 ¢</h3>
    <p class="menu-col__item">Peanut Butter</p><p class="menu-col__item">Almond Butter</p><p class="menu-col__item">Honey</p><p class="menu-col__item">Agave</p>
  </div>

  <div class="abs promo"></div>
  <h2 class="abs centered heading promo__title">ONLY IN FEBRUARY</h2>
  <p class="abs centered promo__offer">GET ONE FREE TOPPING AND DRIZZLE!<br>FRIDAY DELIVERIES ONLY!</p>
  <p class="abs centered fine-print fine-print--menu">* No hidden delivery fees * *5 bowls or smoothies minimum*</p>

  <div class="abs photo-strip" role="img" aria-label="Close-up photo of açaí bowl toppings"></div>
  <p class="abs centered contact contact--menu">(555) 417-9832 | www.berrygoodbites.example | @bgbites</p>

  <div class="abs footer-bars"><span class="footer-bars__main"></span><span class="footer-bars__rest"></span></div>
</section>

</body>
</html>
```